Wix Website design for my therapy business - Willowmere Group

I have started designing a Wix site and have a good idea of what I want.
I have set up the pages, created some design ideas, and inputted the copy. I need someone fabulous to finish off the design aspects. I like working closely with the designers, I was an interior designer in an old career.
I would like the site to be funky but professional. My Wix skills are limited, and I just can't achieve the look I am wanting without having to spend a lot of time learning. If it's easier to start over, that's ok providing you use the same colours, font, images etc. I have included a screenshot of the home page below. I have another site I need to start as soon as we have finished this one.
I am looking for someone who is a good listener and is has design flare. I am easy to get along with and will respond quickly.
I would like to set up SEO and have help in the future.
Let me know if you are the right person for the job.
Target Market(s)
Please needing help with their mental health and for therapy.
Industry/Entity Type
Mental health
Font styles to use
Other font styles liked:
- Futura light
Requirements
Must have
- be easy to navigate and be simple yet stylish
Nice to have
- I have set up the basics of the site - nice to haves are already on the site
Should not have
- old fashioned large chunks of text.

```html
<!DOCTYPE html>
<html lang="en">
<head>
<meta charset="utf-8">
<title>Willowmere Group – Therapy &amp; Counselling</title>
<link href="https://fonts.googleapis.com/css2?family=Jost:wght@300;400;500;600;700&display=swap" rel="stylesheet">
<style>
:root{
  --gold:#a88658;
  --gold-dark:#8a6a40;
  --sand:#c0a27a;
  --tan:#e4d3bd;
  --cream:#f5efe6;
  --cream-2:#efe6da;
  --brown:#5e4522;
  --brown-deep:#3f2c14;
  --ink:#1f1f1f;
  --muted:#555;
  --white:#fff;
}
*{box-sizing:border-box;margin:0;padding:0}
html,body{width:1200px;height:4996px;overflow:hidden}
body{font-family:"Jost",sans-serif;color:var(--ink);background:var(--white);position:relative}
.abs{position:absolute}
a{color:inherit;text-decoration:none}

/* header */
.topbar{left:0;top:0;width:1200px;height:116px;background:var(--white);z-index:5}
.avail{left:108px;top:20px;display:flex;gap:10px;align-items:center}
.avail small{display:block;font-size:11px;color:var(--muted);letter-spacing:.5px}
.avail strong{display:block;font-size:15px;font-weight:500;letter-spacing:1px}
.brand{left:0;width:1200px;top:18px;text-align:center;font-size:27px;font-weight:500;color:var(--gold);letter-spacing:.5px}
.btn-contact{left:970px;top:18px;width:122px;height:34px;border-radius:17px;background:var(--gold);color:var(--white);font-size:14px;display:flex;align-items:center;justify-content:center}
.rule{left:100px;top:68px;width:1012px;height:1px;background:#e6e0d6}
.nav{left:0;top:80px;width:1200px;display:flex;justify-content:center;gap:34px;font-size:14px}
.nav a{position:relative}
.nav a.active{color:var(--gold)}
.nav a.active::after{content:"";position:absolute;left:50%;bottom:-13px;width:4px;height:4px;margin-left:-2px;border-radius:50%;background:var(--gold)}

/* hero */
.hero-photo{left:0;top:116px;width:1200px;height:720px;background:linear-gradient(100deg,#4f6a2e 0%,#7d8f4a 35%,#a7a878 60%,#6f7f3f 100%)}
.hero-sub{left:158px;top:274px;font-size:24px;font-weight:400;color:var(--white)}
.hero-title{left:158px;top:326px;font-size:42px;line-height:50px;font-weight:700;color:var(--white);letter-spacing:.5px}
.btn-help{left:158px;top:468px;width:268px;height:50px;border-radius:25px;background:rgba(138,106,64,.85);color:var(--white);font-size:15px;display:flex;align-items:center;gap:12px;padding-left:28px;letter-spacing:.5px}
.slide-arrow{top:356px;width:44px;height:44px;border:2px solid var(--white);border-radius:50%;display:flex;align-items:center;justify-content:center}

/* about */
.about-photo{left:-56px;top:877px;width:556px;height:556px;border-radius:50%;background:radial-gradient(circle at 60% 40%,#d8b49a 0%,#a5877a 40%,#5d7a8a 80%)}
.eyebrow{font-size:19px;font-weight:400}
.about-eyebrow{left:652px;top:984px}
.h-about{left:652px;top:1016px;font-size:35px;line-height:42px;font-weight:400}
.bar-gold{height:4px;background:var(--gold);border-radius:2px}
.about-text{left:652px;top:1128px;width:380px;font-size:13.5px;line-height:24px;color:#333}
.btn-dark{left:652px;top:1256px;width:168px;height:50px;border-radius:25px;background:var(--ink);color:var(--white);font-size:15px;display:flex;align-items:center;justify-content:center;letter-spacing:.5px}

/* sessions */
.center{left:0;width:1200px;text-align:center}
.sessions-eyebrow{top:1540px;font-size:18px}
.h-section{font-size:31px;font-weight:400;letter-spacing:.5px}
.sessions-title{top:1570px}
.band{left:0;top:1868px;width:1200px;height:813px;background:linear-gradient(180deg,#c0a27a 0%,#bea078 50%,#a7875b 100%)}
.band-photo{left:340px;top:2090px;width:520px;height:591px;background:radial-gradient(ellipse at 50% 40%,rgba(236,214,186,.55) 0%,rgba(192,162,122,0) 70%)}
.card{top:1660px;width:290px;height:435px;background:var(--white);box-shadow:0 4px 18px rgba(0,0,0,.12);border-radius:4px;overflow:hidden}
.card h3{position:absolute;top:40px;left:0;width:100%;text-align:center;font-size:18px;font-weight:700}
.card p{position:absolute;top:80px;left:30px;width:230px;text-align:center;font-size:13px;line-height:21px;color:#444}
.card .go{position:absolute;right:20px;top:190px;width:32px;height:32px;border-radius:50%;background:var(--gold);display:flex;align-items:center;justify-content:center}
.card .pic{position:absolute;left:0;bottom:0;width:100%;height:225px}
.tag{width:238px;height:72px;background:rgba(235,222,204,.88);font-size:19px;display:flex;align-items:center;justify-content:center;border-radius:3px}
.hub{left:456px;top:2258px;width:290px;height:290px;border-radius:50%;background:#efe5d8;display:flex;align-items:center;justify-content:center;font-size:26px;font-weight:500;color:var(--gold)}

/* testimonials */
.testi-eyebrow{top:2756px;font-size:18px}
.testi-title{top:2788px}
.testi-back{left:157px;top:2896px;width:331px;height:344px;background:var(--tan);border-radius:4px}
.testi-photo{left:172px;top:2871px;width:332px;height:352px;border-radius:10px;background:linear-gradient(160deg,#b8c8d3 0%,#d9c1ad 55%,#9fb3c4 100%)}
.quote-mark{left:563px;top:2902px;font-size:60px;line-height:60px;font-weight:700;color:var(--gold)}
.stars{left:612px;top:2917px;font-size:20px;color:#e6a51e;letter-spacing:6px}
.testi-text{left:563px;width:370px;font-size:14px;line-height:22px;color:#333}
.testi-name{left:563px;top:3132px;font-size:21px;font-weight:400}
.avatar{border-radius:50%;background:linear-gradient(160deg,#b9a797,#6f5d50)}

/* questions */
.q-bg{left:0;top:3356px;width:1200px;height:504px;background:var(--cream)}
.q-title{left:170px;top:3460px;width:400px;text-align:center;font-size:26px;line-height:38px;font-weight:700}
.q-text{left:205px;top:3554px;width:330px;text-align:center;font-size:13.5px;line-height:22px;color:#333}
.btn-outline{left:235px;top:3667px;width:272px;height:51px;border-radius:26px;border:2px solid var(--gold);background:var(--white);font-size:16px;display:flex;align-items:center;justify-content:center;gap:12px}
.q-photo{left:640px;top:3386px;width:560px;height:432px;border-radius:216px 0 0 216px;background:linear-gradient(150deg,#f2ede7 0%,#dfe6ec 50%,#c6a27e 100%);border:5px solid var(--tan);border-right:none}

/* what we do */
.what-title{top:3986px;font-size:24px;font-weight:700;color:var(--white)}
.what-text{left:370px;top:4024px;width:460px;text-align:center;font-size:13.5px;line-height:22px;color:#ead9c2}
.step{top:4133px;width:144px;height:144px;border-radius:50%;background:var(--white);display:flex;align-items:center;justify-content:center}
.step.alt{background:var(--gold)}
.step-label{top:4302px;width:200px;text-align:center;font-size:15px;line-height:22px;color:var(--white)}
.btn-start{left:772px;top:4428px;width:213px;height:48px;border-radius:24px;background:var(--gold);color:var(--white);font-size:15px;display:flex;align-items:center;justify-content:center;gap:10px;letter-spacing:.5px}

/* footer */
.foot{left:0;top:4636px;width:1200px;height:360px;background:var(--cream-2)}
.foot-logo{left:108px;top:4690px;width:192px;height:95px;background:var(--white);border-radius:6px;display:flex;align-items:center;justify-content:center;font-size:20px;font-weight:500;color:var(--gold)}
.call-label{left:108px;top:4796px;font-size:16px}
.call-num{left:108px;top:4826px;font-size:24px;font-weight:600;color:var(--gold);letter-spacing:1px}
.vline{top:4668px;width:2px;height:124px;background:var(--tan)}
.foot-col h4{font-size:14px;font-weight:600;color:var(--gold);letter-spacing:1.5px;margin-bottom:10px}
.foot-col li{list-style:none;font-size:13px;line-height:23px;color:#333;letter-spacing:.5px}
.contact-row{display:flex;gap:14px;align-items:flex-start;font-size:14px;line-height:22px;color:#333;letter-spacing:.5px}
.icon-dot{width:26px;height:26px;border-radius:50%;border:1.5px solid var(--gold);display:flex;align-items:center;justify-content:center;flex:none}
.foot-rule{left:108px;top:4912px;width:984px;height:1px;background:#d9ccb9}
.copy{left:108px;top:4930px;font-size:13px;color:#444;letter-spacing:.5px}
.social{top:4926px;width:34px;height:34px;border-radius:50%;background:var(--gold)}
</style>
</head>
<body>

<!-- Header -->
<header class="abs topbar">
  <div class="abs avail">
    <svg width="26" height="26" viewBox="0 0 24 24"><circle cx="12" cy="12" r="12" fill="#6b6b6b"/><path d="M8.5 6.5l2 2-1.2 1.5c.7 1.6 2 2.9 3.6 3.6l1.5-1.2 2 2-1.4 1.6c-3.8-.3-7.4-3.9-7.7-7.7z" fill="#fff"/></svg>
    <div><small>24/7 Available</small><strong>555-014-2290</strong></div>
  </div>
  <div class="abs brand">Willowmere Group</div>
  <a class="abs btn-contact" href="#">Contact</a>
  <div class="abs rule"></div>
  <nav class="abs nav">
    <a class="active" href="#">Home</a><a href="#">About Us</a><a href="#">EMDR</a><a href="#">Addictions</a><a href="#">Betrayal Trauma</a><a href="#">PTSD</a><a href="#">Program List</a><a href="#">Resources</a><a href="#">Blog</a>
  </nav>
</header>

<!-- Hero -->
<section class="hero">
  <div class="abs hero-photo" role="img" aria-label="Woman holding a plank pose on a yoga mat on a sunlit forest path"></div>
  <svg class="abs" style="left:0;top:560px" width="1200" height="340" viewBox="0 0 1200 340">
    <path d="M0 120 C260 110 620 150 1200 270 L1200 340 L0 340 Z" fill="#fff"/>
    <path d="M0 130 C300 120 700 170 1200 265" fill="none" stroke="#f0e7da" stroke-width="26" opacity=".8"/>
    <path d="M380 150 C700 160 950 210 1200 270" fill="none" stroke="#a88658" stroke-width="7"/>
  </svg>
  <div class="abs hero-sub">Willowmere Group</div>
  <h1 class="abs hero-title">THERAPY &amp;<br>COUNSELLING</h1>
  <a class="abs btn-help" href="#">
    <svg width="14" height="14" viewBox="0 0 14 14"><path d="M2 7h10M8 3l4 4-4 4" stroke="#fff" stroke-width="1.6" fill="none"/></svg>
    HOW CAN I HELP YOU
  </a>
  <div class="abs slide-arrow" style="left:62px"><svg width="14" height="14" viewBox="0 0 14 14"><path d="M9 2L4 7l5 5" stroke="#fff" stroke-width="2" fill="none"/></svg></div>
  <div class="abs slide-arrow" style="left:1093px"><svg width="14" height="14" viewBox="0 0 14 14"><path d="M5 2l5 5-5 5" stroke="#fff" stroke-width="2" fill="none"/></svg></div>
</section>

<!-- About -->
<section class="about">
  <div class="abs about-photo" role="img" aria-label="Smiling woman with arms open beside a lake"></div>
  <div class="abs eyebrow about-eyebrow">About Us
    <svg width="80" height="20" viewBox="0 0 80 20" style="vertical-align:middle;margin-left:6px"><path d="M2 14 C20 22 40 4 74 8" stroke="#a88658" stroke-width="1.3" stroke-dasharray="3 3" fill="none"/><path d="M70 4l5 4-6 3" stroke="#a88658" stroke-width="1.3" fill="none"/></svg>
  </div>
  <h2 class="abs h-about">Choose Help.Not<br>Suffering.</h2>
  <div class="abs bar-gold" style="left:652px;top:1110px;width:82px"></div>
  <p class="abs about-text">Lorem Ipsum is simply dummy text of the printing and typesetting industry. Lorem Ipsum has been the industry's standard dummy text ever since the 1500s, when an unknown printer took a galley of type.</p>
  <a class="abs btn-dark" href="#">READ MORE</a>
</section>

<!-- Therapy sessions -->
<section class="sessions">
  <div class="abs center sessions-eyebrow">Therapy Sessions</div>
  <h2 class="abs center h-section sessions-title">Specialized Help For Your Mental Health</h2>
  <div class="abs band"></div>
  <div class="abs band-photo" role="img" aria-label="Woman stretching with arms spread in a golden field"></div>

  <article class="abs card" style="left:138px">
    <h3>PTSD THERAPY</h3>
    <p>Lorem Ipsum is simply dummy text of the printing and typesetting industry. Lorem Ipsum has been the industry's standard</p>
    <span class="go"><svg width="12" height="12" viewBox="0 0 12 12"><path d="M3 9l6-6M4 3h5v5" stroke="#fff" stroke-width="1.5" fill="none"/></svg></span>
    <div class="pic" role="img" aria-label="Therapist listening to a distressed client" style="background:linear-gradient(120deg,#c8908a,#d9c4a6 60%,#8d8aa0)"></div>
    <svg class="abs" style="left:0;top:200px" width="290" height="50" viewBox="0 0 290 50"><path d="M0 0 H290 V34 C200 0 80 -4 0 22 Z" fill="#fff"/><path d="M0 22 C80 -4 200 0 290 34" stroke="#c7aa82" stroke-width="3" fill="none"/></svg>
  </article>
  <article class="abs card" style="left:455px">
    <h3>EMDR THERAPY</h3>
    <p>Lorem Ipsum is simply dummy text of the printing and typesetting industry. Lorem Ipsum has been the industry's standard</p>
    <span class="go"><svg width="12" height="12" viewBox="0 0 12 12"><path d="M3 9l6-6M4 3h5v5" stroke="#fff" stroke-width="1.5" fill="none"/></svg></span>
    <div class="pic" role="img" aria-label="Therapist guiding a client's eye movements with a raised finger" style="background:linear-gradient(120deg,#c7b08e,#2f4c7a 55%,#e6e2dc)"></div>
    <svg class="abs" style="left:0;top:200px" width="290" height="50" viewBox="0 0 290 50"><path d="M0 0 H290 V34 C200 0 80 -4 0 22 Z" fill="#fff"/><path d="M0 22 C80 -4 200 0 290 34" stroke="#c7aa82" stroke-width="3" fill="none"/></svg>
  </article>
  <article class="abs card" style="left:783px">
    <h3>RELATIONSHIPS</h3>
    <p>Lorem Ipsum is simply dummy text of the printing and typesetting industry. Lorem Ipsum has been the industry's standard</p>
    <span class="go"><svg width="12" height="12" viewBox="0 0 12 12"><path d="M3 9l6-6M4 3h5v5" stroke="#fff" stroke-width="1.5" fill="none"/></svg></span>
    <div class="pic" role="img" aria-label="Couple sitting together sharing a warm moment" style="background:linear-gradient(120deg,#d9c7b5,#a76f56 50%,#e7e5e2)"></div>
    <svg class="abs" style="left:0;top:200px" width="290" height="50" viewBox="0 0 290 50"><path d="M0 0 H290 V34 C200 0 80 -4 0 22 Z" fill="#fff"/><path d="M0 22 C80 -4 200 0 290 34" stroke="#c7aa82" stroke-width="3" fill="none"/></svg>
  </article>

  <svg class="abs" style="left:0;top:2180px" width="1200" height="460" viewBox="0 0 1200 460">
    <g stroke="#f4ece0" stroke-width="2" fill="#f4ece0">
      <line x1="440" y1="44" x2="520" y2="130"/><line x1="440" y1="124" x2="470" y2="170"/><line x1="440" y1="204" x2="460" y2="210"/><line x1="440" y1="284" x2="470" y2="262"/><line x1="440" y1="364" x2="520" y2="300"/>
      <line x1="760" y1="44" x2="680" y2="130"/><line x1="760" y1="124" x2="730" y2="170"/><line x1="760" y1="204" x2="740" y2="210"/><line x1="760" y1="284" x2="730" y2="262"/><line x1="760" y1="364" x2="680" y2="300"/>
      <circle cx="440" cy="44" r="5"/><circle cx="440" cy="124" r="5"/><circle cx="440" cy="204" r="5"/><circle cx="440" cy="284" r="5"/><circle cx="440" cy="364" r="5"/>
      <circle cx="760" cy="44" r="5"/><circle cx="760" cy="124" r="5"/><circle cx="760" cy="204" r="5"/><circle cx="760" cy="284" r="5"/><circle cx="760" cy="364" r="5"/>
    </g>
  </svg>
  <div class="abs tag" style="left:162px;top:2188px">EMDR Therapy</div>
  <div class="abs tag" style="left:162px;top:2268px">PTSD Therapy</div>
  <div class="abs tag" style="left:162px;top:2348px">Relationships</div>
  <div class="abs tag" style="left:162px;top:2428px">Trauma Informed</div>
  <div class="abs tag" style="left:162px;top:2508px">Equine Therapy</div>
  <div class="abs tag" style="left:800px;top:2184px">Hawkesbury</div>
  <div class="abs tag" style="left:800px;top:2264px">Based</div>
  <div class="abs tag" style="left:800px;top:2344px">Anxiety &amp;</div>
  <div class="abs tag" style="left:800px;top:2424px">Depression</div>
  <div class="abs tag" style="left:800px;top:2504px">Addiction</div>
  <div class="abs hub">Willowmere</div>
</section>

<!-- Testimonials -->
<section class="testimonials">
  <div class="abs center testi-eyebrow">Testimonials</div>
  <h2 class="abs center h-section testi-title">Love where you live.</h2>
  <div class="abs testi-back"></div>
  <div class="abs testi-photo" role="img" aria-label="Relaxed woman smiling with hands behind her head"></div>
  <div class="abs quote-mark">&ldquo;</div>
  <div class="abs stars">★★★★★</div>
  <p class="abs testi-text" style="top:2964px">Lorem Ipsum is simply dummy text of the printing and typesetting industry lorem Ipsum..........</p>
  <p class="abs testi-text" style="top:3022px">Lorem Ipsum is simply dummy text of the printing and typesetting industry. Lorem Ipsum has been the industry's standard dummy text ever since the 1500s, when an unknown printer took.</p>
  <div class="abs testi-name">- OWEN R.</div>
  <div class="abs avatar" style="left:990px;top:2950px;width:40px;height:40px" role="img" aria-label="Reviewer portrait"></div>
  <div class="abs" style="left:983px;top:3002px;width:56px;height:56px;border-radius:50%;border:3px solid var(--gold);padding:3px"><div class="avatar" style="width:100%;height:100%" role="img" aria-label="Featured reviewer portrait"></div></div>
  <div class="abs avatar" style="left:990px;top:3072px;width:40px;height:40px" role="img" aria-label="Reviewer portrait"></div>
</section>

<!-- Questions -->
<section class="questions">
  <div class="abs q-bg"></div>
  <svg class="abs" style="left:0;top:3356px" width="700" height="504" viewBox="0 0 700 504">
    <path d="M0 330 C180 250 360 330 560 460 C600 490 640 504 700 504 L0 504 Z" fill="#fff"/>
  </svg>
  <h2 class="abs q-title">Have Questions? Marigold<br>Support Has You Covered.</h2>
  <p class="abs q-text">Lorem Ipsum is simply dummy text of the printing and typesetting industry. Lorem Ipsum has been the industry's standard</p>
  <a class="abs btn-outline" href="#">
    <svg width="14" height="14" viewBox="0 0 14 14"><path d="M2 7h10M8 3l4 4-4 4" stroke="#a88658" stroke-width="1.6" fill="none"/></svg>
    HOW CAN I HELP YOU
  </a>
  <svg class="abs" style="left:455px;top:3730px" width="130" height="50" viewBox="0 0 130 50"><path d="M8 6 C10 40 60 44 118 22" stroke="#a88658" stroke-width="1.3" stroke-dasharray="3 3" fill="none"/><path d="M112 16l7 6-8 4" stroke="#a88658" stroke-width="1.3" fill="none"/></svg>
  <div class="abs q-photo" role="img" aria-label="Smiling woman in a light blue shirt pointing to the side"></div>
</section>

<!-- What we do -->
<section class="what">
  <svg class="abs" style="left:0;top:3856px" width="1200" height="790" viewBox="0 0 1200 790">
    <defs><linearGradient id="brownFade" x1="0" y1="0" x2="0" y2="1"><stop offset="0" stop-color="#5e4522"/><stop offset=".6" stop-color="#6d522c"/><stop offset="1" stop-color="#a5865c"/></linearGradient></defs>
    <path d="M0 4 L1200 60 L1200 790 L0 790 Z" fill="url(#brownFade)"/>
    <path d="M0 560 C300 640 800 640 1200 560 L1200 790 L0 790 Z" fill="#efe6da"/>
    <path d="M0 545 C350 660 850 650 1200 550" fill="none" stroke="#fff" stroke-width="10"/>
    <path d="M0 592 C350 680 850 668 1200 590" fill="none" stroke="#c0a27a" stroke-width="4"/>
  </svg>
  <h2 class="abs center what-title">What We Do</h2>
  <p class="abs what-text">Lorem Ipsum is simply dummy text of the printing and typesetting industry. Lorem Ipsum has been the industry's standard</p>
  <div class="abs bar-gold" style="left:575px;top:4074px;width:50px;height:3px;background:#c9ad86"></div>

  <svg class="abs" style="left:300px;top:4100px" width="600" height="170" viewBox="0 0 600 170">
    <path d="M60 40 C120 0 200 0 220 34" stroke="#d9c3a2" stroke-width="1.5" stroke-dasharray="5 4" fill="none"/>
    <path d="M214 26l7 9-10 2" stroke="#d9c3a2" stroke-width="1.5" fill="none"/>
    <path d="M350 150 C420 190 500 170 530 140" stroke="#d9c3a2" stroke-width="1.5" stroke-dasharray="5 4" fill="none"/>
    <path d="M522 138l9 1-3 9" stroke="#d9c3a2" stroke-width="1.5" fill="none"/>
  </svg>

  <div class="abs step" style="left:228px">
    <svg width="70" height="70" viewBox="0 0 70 70" fill="none" stroke="#a88658" stroke-width="2.4"><rect x="14" y="12" width="34" height="46" rx="3"/><rect x="24" y="8" width="14" height="8" rx="2"/><path d="M21 26h20M21 34h20M21 42h12"/><circle cx="50" cy="48" r="11" fill="#fff"/><path d="M45 48l4 4 7-8"/></svg>
  </div>
  <div class="abs step alt" style="left:529px">
    <svg width="74" height="70" viewBox="0 0 74 70" fill="none" stroke="#fff" stroke-width="2.4"><circle cx="20" cy="16" r="6"/><circle cx="54" cy="16" r="6"/><path d="M20 24v18h-10v20M54 24v18h10v20M28 42h18M37 42v20M8 30v32M66 30v32"/></svg>
  </div>
  <div class="abs step" style="left:828px">
    <svg width="74" height="70" viewBox="0 0 74 70" fill="none" stroke="#a88658" stroke-width="2.4"><rect x="10" y="8" width="54" height="26"/><path d="M10 16h54M10 24h54"/><circle cx="30" cy="36" r="5"/><path d="M22 44l10 4 14-6 8 10M26 58h32M40 48v10"/></svg>
  </div>
  <div class="abs step-label" style="left:200px">Book A<br>Counselling</div>
  <div class="abs step-label" style="left:501px">Choose A Counselor<br>&amp; Pick A Time</div>
  <div class="abs step-label" style="left:800px">Relax</div>
  <a class="abs btn-start" href="#">
    <svg width="14" height="14" viewBox="0 0 14 14"><path d="M2 7h10M8 3l4 4-4 4" stroke="#fff" stroke-width="1.6" fill="none"/></svg>
    GET STARTED !
  </a>
</section>

<!-- Footer -->
<footer>
  <div class="abs foot"></div>
  <div class="abs foot-logo">Willowmere Group</div>
  <div class="abs call-label">Call now for questions</div>
  <div class="abs call-num">1300 555 010</div>
  <div class="abs vline" style="left:376px"></div>
  <div class="abs vline" style="left:614px"></div>
  <div class="abs vline" style="left:836px"></div>
  <div class="abs foot-col" style="left:406px;top:4672px">
    <h4>NAVIGATION</h4>
    <ul><li>Home</li><li>About Us</li><li>EMDR</li><li>Addictions</li><li>Betrayal Trauma</li></ul>
  </div>
  <div class="abs foot-col" style="left:642px;top:4672px">
    <h4>NAVIGATION</h4>
    <ul><li>PTSD</li><li>Program List</li><li>Resources</li><li>Blog</li><li>Contact Us</li></ul>
  </div>
  <div class="abs foot-col" style="left:866px;top:4672px">
    <h4>CONTACT &nbsp;INFORMATION</h4>
    <div class="contact-row" style="margin-top:4px"><span class="icon-dot"><svg width="12" height="14" viewBox="0 0 12 14"><path d="M6 13s5-5 5-8A5 5 0 0 0 1 5c0 3 5 8 5 8z" stroke="#a88658" stroke-width="1.3" fill="none"/><circle cx="6" cy="5" r="1.8" fill="#a88658"/></svg></span><span>233 Street 111, Suite 1<br>Address, City</span></div>
    <div class="contact-row" style="margin-top:12px"><span class="icon-dot"><svg width="12" height="12" viewBox="0 0 12 12"><path d="M2 1.5l2.2 2.2-1 1.3c.6 1.3 1.6 2.3 2.9 2.9l1.3-1 2.2 2.2-1.3 1.4C5 10.3 1.7 7 1.5 3z" fill="#a88658"/></svg></span><span>8888 888 888</span></div>
    <div class="contact-row" style="margin-top:18px"><span class="icon-dot"><svg width="12" height="10" viewBox="0 0 12 10"><rect x=".7" y=".7" width="10.6" height="8.6" stroke="#a88658" stroke-width="1.3" fill="none"/><path d="M1 1l5 4 5-4" stroke="#a88658" stroke-width="1.3" fill="none"/></svg></span><span>name@company.com</span></div>
  </div>
  <div class="abs foot-rule"></div>
  <div class="abs copy">Copyright © 2023 Willowmere Group. All rights reserved.</div>
  <span class="abs social" style="left:917px" aria-label="Social profile"></span>
  <span class="abs social" style="left:962px" aria-label="Social profile"></span>
  <span class="abs social" style="left:1006px" aria-label="Social profile"></span>
</footer>

</body>
</html>
```